Professional & attention grabbing.

A business card design, front and back. I already have a logo I will attach, but I am open to something new as well.
Things to include:
Name:
Title:
Phone:
Email:
Wanting something that is professional but attention grabbing.
Also we do a lot of work using drones on natural gas pipelines (leading the future)if you want to include any of that. I'm open to ideas.
Target Market(s)
Natural gas transmission industry / greenhouse gas mitigation industry
Industry/Entity Type
Business
Contact Information for Business Card
All details have been conveyed above.
Colors
Designer to choose colors to be used in the design.
Look and feel
Each slider illustrates characteristics of the customer's brand and the style your logo design should communicate.

```html
<!DOCTYPE html>
<html lang="en">
<head>
<meta charset="utf-8">
<title>Veridan Inspections – Business Card</title>
<link rel="stylesheet" href="https://fonts.googleapis.com/css2?family=Open+Sans:wght@400;600;700;800&display=swap">
<style>
  :root {
    --backdrop: #3a3431;
    --card: #1b1b1c;
    --card-edge: #111112;
    --white: #f2f2f2;
    --red: #d4262c;
    --muted: #6e6e70;
    --emboss: #2c2c2e;
    --divider: #8a8a8c;
  }
  * { box-sizing: border-box; margin: 0; padding: 0; }
  html, body {
    width: 1200px; height: 864px; overflow: hidden;
    background: var(--backdrop);
    font-family: "Open Sans", Arial, sans-serif;
  }
  .canvas { position: relative; width: 1200px; height: 864px; }
  .card {
    position: absolute;
    width: 525px; height: 300px;
    background: var(--card);
    border: 1px solid var(--card-edge);
    box-shadow: 0 12px 30px rgba(0,0,0,.45);
  }
  /* Back side */
  .card--back { left: 70px; top: 70px; }
  .back-mark {
    position: absolute; left: 50%; top: 52px; transform: translateX(-50%);
    display: flex; align-items: center; gap: 14px;
  }
  .back-mark__square { width: 60px; height: 60px; background: var(--emboss); }
  .back-mark__name {
    font-weight: 800; font-size: 54px; color: var(--emboss); letter-spacing: 1px;
  }
  .back-web {
    position: absolute; left: 0; right: 0; bottom: 70px; text-align: center;
    color: var(--muted); font-size: 14px; letter-spacing: 6px;
  }
  /* Front side */
  .card--front { left: 605px; top: 494px; }
  .brand {
    position: absolute; left: 40px; top: 108px;
    display: flex; align-items: center; gap: 12px;
  }
  .brand__square { width: 22px; height: 22px; background: var(--red); }
  .brand__name {
    font-weight: 800; font-size: 27px; line-height: 1.05; color: var(--white);
  }
  .divider {
    position: absolute; left: 262px; top: 88px; width: 1px; height: 124px;
    background: var(--divider);
  }
  .contact { position: absolute; left: 284px; top: 88px; color: var(--white); }
  .contact__name { color: var(--red); font-weight: 600; font-size: 19px; line-height: 1.1; }
  .contact__title { font-size: 16px; margin-bottom: 12px; }
  .contact__row {
    display: flex; align-items: center; gap: 10px;
    font-size: 14px; line-height: 22px;
  }
  .contact__row svg { width: 14px; height: 14px; flex: none; }
</style>
</head>
<body>
<div class="canvas">

  <section class="card card--back" aria-label="Card back">
    <div class="back-mark">
      <span class="back-mark__square"></span>
      <span class="back-mark__name">VERIDAN</span>
    </div>
    <p class="back-web">www.veridan.example</p>
  </section>

  <section class="card card--front" aria-label="Card front">
    <div class="brand">
      <span class="brand__square"></span>
      <span class="brand__name">Veridan<br>Inspections</span>
    </div>
    <div class="divider"></div>
    <div class="contact">
      <p class="contact__name">Mark Elden</p>
      <p class="contact__title">President</p>
      <p class="contact__row">
        <svg viewBox="0 0 16 16" aria-hidden="true"><path fill="#d4262c" d="M3 1h3l1.5 4-2 1.2a8 8 0 0 0 4.3 4.3L11 8.5l4 1.5v3a2 2 0 0 1-2 2A12 12 0 0 1 1 3a2 2 0 0 1 2-2z"/></svg>
        555 0148 2297
      </p>
      <p class="contact__row">
        <svg viewBox="0 0 16 16" aria-hidden="true"><rect x="1" y="3" width="14" height="10" fill="#d4262c"/><path d="M1 3l7 6 7-6" fill="none" stroke="#1b1b1c" stroke-width="1.4"/></svg>
        mark@veridan.example
      </p>
      <p class="contact__row">
        <svg viewBox="0 0 16 16" aria-hidden="true"><circle cx="8" cy="8" r="7" fill="#d4262c"/><circle cx="8" cy="7" r="2.2" fill="#1b1b1c"/></svg>
        www.veridan.example
      </p>
    </div>
  </section>

</div>
</body>
</html>
```